Bref créative
Corporate Advisory
Professional
Dorian Pelhame
Director
Level 6, 412 Brindle Street, Spring Hill. QLD 4000
dorian.pelhame@veltrina.com.au
www.veltrina.com.au
Corporate colours are the blue and white in logo. Front may be one colour eg white with blue logo and rear may be blue with white logo
Can be as simple as blue background and white logo
Veltrina logo - white background with blue logo is primary and blue background with white logo is secondary - no other coloures used.

```html
<!DOCTYPE html>
<html lang="en">
<head>
<meta charset="utf-8">
<title>Veltrina Stationery Suite</title>
<link href="https://fonts.googleapis.com/css2?family=Raleway:wght@300;400;600&display=swap" rel="stylesheet">
<style>
  :root {
    --navy: #1c3a5e;
    --navy-deep: #15304f;
    --white: #ffffff;
    --paper: #fbfcfd;
    --grey: #d6dade;
    --grey-mid: #b9c0c7;
    --ghost: #e9edf1;
    --ink: #33475c;
    --canvas: #ffffff;
  }
  * { box-sizing: border-box; margin: 0; padding: 0; }
  html, body { width: 1200px; height: 1091px; overflow: hidden; background: var(--canvas); }
  body { position: relative; font-family: "Raleway", sans-serif; color: var(--ink); }

  .piece { position: absolute; background: var(--paper); box-shadow: 0 2px 6px rgba(0,0,0,.18); overflow: hidden; }

  .brand { display: flex; align-items: center; gap: 8px; }
  .brand-square { width: 22px; height: 22px; background: var(--navy); flex: none; }
  .brand-name { font-weight: 300; font-size: 30px; letter-spacing: 1px; color: var(--navy); line-height: 1; }
  .brand-tag { font-size: 6px; letter-spacing: 1.5px; text-transform: uppercase; color: var(--navy); margin-top: 3px; }
  .brand.on-dark .brand-square { background: var(--white); }
  .brand.on-dark .brand-name, .on-dark .brand-tag { color: var(--white); }

  .motif { position: absolute; background: radial-gradient(ellipse at 55% 45%, var(--ghost) 0%, rgba(233,237,241,.6) 45%, rgba(233,237,241,0) 72%); }
  .motif.on-dark { background: radial-gradient(ellipse at 55% 45%, rgba(255,255,255,.09) 0%, rgba(255,255,255,0) 70%); }

  /* Letterhead */
  .letterhead { left: 44px; top: 44px; width: 581px; height: 729px; }
  .letterhead .edge-mark { position: absolute; left: 0; top: 15px; width: 12px; height: 44px; background: var(--navy); }
  .letterhead .brand { position: absolute; left: 30px; top: 22px; }
  .letterhead .motif { left: 280px; top: 230px; width: 300px; height: 420px; }
  .letterhead .footer-grey { position: absolute; left: 0; bottom: 12px; width: 140px; height: 80px; background: var(--grey); }
  .letterhead .footer-band { position: absolute; left: 140px; bottom: 12px; right: 0; height: 80px; background: var(--navy); display: flex; gap: 40px; padding: 18px 22px; color: var(--white); font-size: 9px; line-height: 1.5; }

  /* Business cards */
  .card-front { left: 162px; top: 186px; width: 245px; height: 183px; }
  .card-front .brand { position: absolute; left: 14px; top: 18px; }
  .card-front .brand-name { font-size: 22px; }
  .card-front .brand-square { width: 16px; height: 16px; }
  .card-front .holder { position: absolute; left: 44px; top: 70px; }
  .card-front .holder-name { font-size: 15px; color: var(--navy); font-weight: 400; }
  .card-front .holder-role { font-size: 9px; color: var(--navy); margin-bottom: 8px; }
  .card-front .holder-contact { font-size: 6.5px; line-height: 1.6; color: var(--ink); }
  .card-front .motif { right: -20px; bottom: -10px; width: 120px; height: 120px; }

  .card-back { left: 15px; top: 319px; width: 242px; height: 147px; background: var(--navy); }
  .card-back .brand { position: absolute; left: 78px; top: 42px; flex-direction: column; gap: 6px; }
  .card-back .brand-square { width: 22px; height: 22px; }
  .card-back .brand-tag { font-size: 5.5px; text-align: center; margin-top: 0; }

  /* Envelopes */
  .envelope-back { left: 398px; top: 44px; width: 776px; height: 334px; background: var(--white); }
  .envelope-back .flap { position: absolute; left: 0; top: 0; width: 100%; height: 100%; }
  .envelope-back .brand { position: absolute; left: 300px; top: 24px; }
  .envelope-back .brand-name { font-size: 26px; }
  .envelope-back .brand-square { width: 18px; height: 18px; }

  .envelope-front { left: 531px; top: 183px; width: 634px; height: 342px; }
  .envelope-front .top-band { position: absolute; left: 0; top: 0; width: 100%; height: 18px; background: var(--navy); }
  .envelope-front .brand { position: absolute; left: 30px; top: 50px; }
  .envelope-front .brand-name { font-size: 32px; }
  .envelope-front .return-line { position: absolute; left: 30px; top: 104px; font-size: 7px; color: var(--ink); letter-spacing: .3px; }
  .envelope-front .motif { right: -20px; top: 40px; width: 320px; height: 300px; }

  /* Slides */
  .slide { top: 790px; width: 377px; height: 213px; }
  .slide-title { left: 15px; }
  .slide-title .brand { position: absolute; left: 14px; top: 22px; }
  .slide-title .brand-name { font-size: 22px; }
  .slide-title .brand-square { width: 16px; height: 16px; }
  .slide-title .motif { right: -10px; top: 20px; width: 200px; height: 190px; }
  .slide-title .title-band { position: absolute; left: 18px; right: 0; top: 168px; height: 25px; background: var(--navy); color: var(--white); font-size: 16px; padding: 3px 12px; text-transform: uppercase; letter-spacing: .5px; }
  .slide-title .title-band b { font-weight: 600; text-transform: none; }
  .slide-title .subtitle { position: absolute; left: 18px; top: 197px; width: 100px; height: 14px; background: var(--grey-mid); color: var(--white); font-size: 8px; padding: 2px 10px; }

  .slide-page { left: 407px; }
  .slide-page .brand { position: absolute; left: 10px; top: 10px; gap: 4px; }
  .slide-page .brand-name { font-size: 10px; }
  .slide-page .brand-square { width: 8px; height: 8px; }
  .slide-page .page-label { position: absolute; left: 22px; top: 40px; background: var(--navy); color: var(--white); font-size: 12px; padding: 5px 14px; }
  .slide-page .motif { right: -10px; top: 30px; width: 200px; height: 190px; }
  .slide-page .foot { position: absolute; left: 0; right: 0; bottom: 0; height: 5px; background: var(--navy); }

  .slide-insert { left: 805px; width: 375px; background: var(--navy-deep); }
  .slide-insert .motif { right: -10px; top: 20px; width: 220px; height: 200px; }
  .slide-insert .insert-label { position: absolute; left: 12px; top: 82px; background: var(--grey); color: var(--navy); font-size: 12px; padding: 4px 12px; }
  .slide-insert .insert-copy { position: absolute; left: 18px; top: 110px; width: 180px; font-size: 7px; line-height: 1.6; color: var(--white); }
</style>
</head>
<body>

<section class="piece letterhead">
  <div class="edge-mark"></div>
  <div class="brand">
    <span class="brand-square"></span>
    <div>
      <div class="brand-name">VELTRINA</div>
      <div class="brand-tag">Professional Corporate Advisory</div>
    </div>
  </div>
  <div class="motif" role="img" aria-label="Faint large brand emblem watermark"></div>
  <div class="footer-grey"></div>
  <div class="footer-band">
    <div>Level 6, 412 Brindle Street<br>Spring Hill. QLD 4000<br>P 07 3100 4826<br>F 07 3100 4827</div>
    <div>dorian.pelhame@veltrina.com.au<br>www.veltrina.com.au</div>
  </div>
</section>

<section class="piece envelope-back">
  <svg class="flap" viewBox="0 0 776 334" preserveAspectRatio="none" aria-hidden="true">
    <path d="M0 0 H776 V90 L700 105 H76 L0 90 Z" fill="var(--navy)"/>
  </svg>
  <div class="brand on-dark">
    <span class="brand-square"></span>
    <div class="brand-name">VELTRINA</div>
  </div>
</section>

<section class="piece envelope-front">
  <div class="top-band"></div>
  <div class="brand">
    <span class="brand-square"></span>
    <div>
      <div class="brand-name">VELTRINA</div>
      <div class="brand-tag">Professional Corporate Advisory</div>
    </div>
  </div>
  <div class="return-line">Level 6, 412 Brindle Street, Spring Hill. QLD 4000 &nbsp;·&nbsp; P 07 3100 4826 &nbsp;·&nbsp; www.veltrina.com.au</div>
  <div class="motif" role="img" aria-label="Faint large brand emblem watermark"></div>
</section>

<section class="piece card-front">
  <div class="brand">
    <span class="brand-square"></span>
    <div>
      <div class="brand-name">VELTRINA</div>
      <div class="brand-tag">Professional Corporate Advisory</div>
    </div>
  </div>
  <div class="motif" role="img" aria-label="Faint brand emblem watermark"></div>
  <div class="holder">
    <div class="holder-name">Dorian Pelhame</div>
    <div class="holder-role">Director</div>
    <div class="holder-contact">P 07 3100 4826<br>dorian.pelhame@veltrina.com.au<br>www.veltrina.com.au</div>
  </div>
</section>

<section class="piece card-back">
  <div class="brand on-dark">
    <span class="brand-square"></span>
    <div class="brand-tag">Professional Corporate Advisory</div>
  </div>
</section>

<section class="piece slide slide-title">
  <div class="brand">
    <span class="brand-square"></span>
    <div>
      <div class="brand-name">VELTRINA</div>
      <div class="brand-tag">Professional Corporate Advisory</div>
    </div>
  </div>
  <div class="motif" role="img" aria-label="Faint large brand emblem watermark"></div>
  <div class="title-band"><b>TITLE</b> of PRESENTATION</div>
  <div class="subtitle">Sub-title</div>
</section>

<section class="piece slide slide-page">
  <div class="brand">
    <span class="brand-square"></span>
    <div class="brand-name">VELTRINA</div>
  </div>
  <div class="page-label">Title of Page X</div>
  <div class="motif" role="img" aria-label="Faint large brand emblem watermark"></div>
  <div class="foot"></div>
</section>

<section class="piece slide slide-insert">
  <div class="motif on-dark" role="img" aria-label="Faint large brand emblem watermark"></div>
  <div class="insert-label">Title of Insert Page</div>
  <p class="insert-copy">Content for this insert page goes here in brief paragraph form, summarising the key advisory points for the client.</p>
</section>

</body>
</html>
```